Private Gym Needs a Rack Card Design

We need a basic front and back rack card (same size as post card) that gives basic information about our brand, and includes our logo. Please see attached logo and required content below.

Target Market(s)

Upscale, private gym.

Industry/Entity Type

Gym

Font styles to use
Sans Serif

Colors
ffffff
5c5c5c
000000
dbdbdb
f78f20

Requirements
Must have
• Business Logo and the following text in a clean, modern, easy-to-read, artistic manner. Style and design must be clean, incorporate our color scheme of MOSTLY white, light grey, charcoal, with just pops of orange. We want the card itself to be mostly white background. Must include website URL as well: corevantagestudio.com
• FRONT CARD:
• Logo
• A safe and individualized approach to exercise
• Our method employs the latest weight resistance training exercises and coaching for healthy living. Not only is our workout methodology effective, it’s safe.
• Our Method…
• -Improves Functional Movement
• -Promotes Weight Loss
• -Builds Strength
• -Increases Flexibility 

• BACK:
• Change Your Body. Find Your Strength.
• There’s 40 years of success behind our proven method
• What is The Formwell? 
• The Formwell is all about teaching our clients how to lift weights and exercise with the proper technique. There’s no slinging or jerking at our gym; only controlled movements that yield real results.
• Come workout with us in our private gym. We are located in Durham adjacent to Harlow Campus and 5 minutes from downtown Durham.
• Address: 482 Linden Ave, Durham, NC 27705
• Phone: (919) 555-2741
• Hours: 9:00 AM – 9:00 PM
Nice to have
• Great organization of text, maybe some columns, colored bullet points, cool graphics and logos.
Should not have
• Busy or crowded design. All lines should be sleek, straight, and streamline. NO STOCK IMAGES, but logos are GREAT

```html
<!DOCTYPE html>
<html lang="en">
<head>
<meta charset="utf-8">
<title>The Formwell – Rack Card Front</title>
<link rel="stylesheet" href="https://fonts.googleapis.com/css2?family=Barlow+Condensed:wght@400;500;600&family=Montserrat:wght@700&display=swap">
<style>
  :root {
    --backdrop: #838488;
    --card: #ffffff;
    --charcoal: #5c5c5c;
    --orange: #f26633;
    --rule: #6b6b6b;
  }
  html, body {
    margin: 0;
    width: 1200px;
    height: 1200px;
    overflow: hidden;
    background: var(--backdrop);
  }
  .rack-card {
    position: absolute;
    left: 92px;
    top: 240px;
    width: 1016px;
    height: 720px;
    background: var(--card);
  }
  .rack-card svg { display: block; }
  .brand-name {
    font-family: "Montserrat", sans-serif;
    font-weight: 700;
    fill: var(--charcoal);
  }
  .tagline {
    font-family: "Barlow Condensed", sans-serif;
    font-weight: 500;
    fill: var(--card);
  }
  .statement {
    font-family: "Barlow Condensed", sans-serif;
    font-weight: 600;
    fill: var(--charcoal);
  }
  .benefit {
    font-family: "Barlow Condensed", sans-serif;
    font-weight: 500;
    fill: var(--orange);
  }
  .band { fill: var(--orange); }
  .frame-line {
    fill: none;
    stroke: var(--rule);
    stroke-width: 1.2;
  }
</style>
</head>
<body>
  <section class="rack-card">
    <svg width="1016" height="720" viewBox="92 240 1016 720" xmlns="http://www.w3.org/2000/svg">
      <!-- brand -->
      <rect class="brand-mark" x="188" y="322" width="22" height="22" fill="var(--orange)"/>
      <text class="brand-name" x="222" y="386" font-size="66" textLength="382" lengthAdjust="spacingAndGlyphs">The Formwell</text>

      <!-- tagline band -->
      <rect class="band" x="92" y="461" width="740" height="58"/>
      <rect class="band" x="858" y="461" width="214" height="58"/>
      <text class="tagline" x="184" y="498" font-size="25">A safe and individualized approach to exercise</text>

      <!-- frame lines -->
      <polyline class="frame-line" points="130,542 130,922 1069,922 1069,556"/>
      <polyline class="frame-line" points="674,886 674,554 844,554 844,362 653,362"/>
      <polyline class="frame-line" points="662,355 653,362 662,369"/>
      <rect x="672" y="884" width="4" height="4" fill="var(--rule)"/>

      <!-- statement -->
      <text class="statement" x="184" y="588" font-size="50" textLength="416" lengthAdjust="spacingAndGlyphs">OUR METHOD EMPLOYS</text>
      <text class="statement" x="184" y="618" font-size="27" textLength="416" lengthAdjust="spacingAndGlyphs">THE LATEST WEIGHT RESISTANCE TRAINING</text>
      <text class="statement" x="184" y="660" font-size="45" textLength="416" lengthAdjust="spacingAndGlyphs">EXERCISES AND COACHING</text>
      <text class="statement" x="184" y="704" font-size="54" textLength="416" lengthAdjust="spacingAndGlyphs">FOR HEALTHY LIVING.</text>
      <text class="statement" x="184" y="760" font-size="66" textLength="416" lengthAdjust="spacingAndGlyphs">NOT ONLY IS OUR</text>
      <text class="statement" x="184" y="794" font-size="31" textLength="416" lengthAdjust="spacingAndGlyphs">WORKOUT METHODOLOGY EFFECTIVE,</text>
      <text class="statement" x="184" y="886" font-size="108" textLength="418" lengthAdjust="spacingAndGlyphs">IT’S SAFE.</text>

      <!-- benefits -->
      <g class="benefit-arrows">
        <polyline class="frame-line" points="674,652 699,652"/><polyline class="frame-line" points="692,645 699,652 692,659"/>
        <polyline class="frame-line" points="674,699 699,699"/><polyline class="frame-line" points="692,692 699,699 692,706"/>
        <polyline class="frame-line" points="674,746 699,746"/><polyline class="frame-line" points="692,739 699,746 692,753"/>
        <polyline class="frame-line" points="674,793 699,793"/><polyline class="frame-line" points="692,786 699,793 692,800"/>
      </g>
      <text class="benefit" x="708" y="659" font-size="25">Improves Functional Movement</text>
      <text class="benefit" x="708" y="706" font-size="25">Promotes Weight Loss</text>
      <text class="benefit" x="708" y="753" font-size="25">Builds Strength</text>
      <text class="benefit" x="708" y="800" font-size="25">Increases Flexibility</text>
    </svg>
  </section>
</body>
</html>
```